Fennel Cellar Online organic artisan and gourmet supermarket

Brief:
Brand: Fennel Cellar (FC) is an online store selling artisan and organinc Italian products. Our look and feel we have gone with is rustic, premium and unfiltered (visit us @ www.fennelcellar.com.au)
Our slogan: "cook Italy, eat Italy, love Italy"
Goals: prior to our online store going live, we used to attend a food market once a week. Due to unfortunate circumstances, we stopped. Since then, our store has gone live and wanted to use the card as a reminder we are back at the markets.
I also have a restaurant, "fennel ristorante" so I wanted to hand them out to customers in the restaurant but also act as reminder of our pop up market stores and our website to buy from.
Personality: FC is more than just a store. Our goal is to be not only a store but an informationa hub of Italian food.
We offer assistance to people who need help in their kitchen as well as catering
Logo: I have a logo which I was not able to upload.

Target Market(s)

Food lovers
Italian food interest
Wealthy
Organic gourmet food enthusiest

Industry/Entity Type

Store

Contact Information for Business Card

Shop online or visit us @ Willow Bend organic market
Ciao@fennelcellar.com.au
Www.fennelcellar.com.au

Online store, Cooking advice, catering, ristorante and information hub

Requirements
Must have
• Logo
• Information
• May be larger than a business card to fit information but smaller than a post card
• Need to look interesting and different
• Not a simple card design
Nice to have
• Different fonts
• Rustic looking
• Qwerky

```html
<!DOCTYPE html>
<html lang="en">
<head>
<meta charset="utf-8">
<title>Fennel Cellar – Market Card</title>
<link rel="stylesheet" href="https://fonts.googleapis.com/css2?family=Oswald:wght@500;700&family=Montserrat:wght@400&family=Share+Tech+Mono&display=swap">
<style>
  :root {
    --backdrop: #dcdcdc;
    --card-white: #f7f7f5;
    --rim: #2a2a2a;
    --leaf: #cddf8d;
    --forest: #1c7a43;
    --ink: #1a1a1a;
    --tag-text: #d8e98a;
    --paper-white: #ffffff;
  }
  * { margin: 0; padding: 0; box-sizing: border-box; }
  html, body { width: 1200px; height: 720px; overflow: hidden; background: var(--backdrop); }
  .canvas {
    position: relative; width: 1200px; height: 720px;
    display: flex; align-items: center; justify-content: center; gap: 80px;
  }
  .card {
    position: relative; width: 470px; height: 470px; border-radius: 50%; overflow: hidden;
  }

  /* Front: brand side */
  .card--front {
    background: var(--card-white);
    border: 5px solid var(--rim);
    display: flex; align-items: center; justify-content: center; gap: 16px;
  }
  .brand-dot { width: 22px; height: 22px; border-radius: 50%; background: var(--forest); }
  .brand-name {
    font-family: 'Oswald', sans-serif; font-weight: 500; font-size: 52px;
    letter-spacing: 3px; text-transform: uppercase; color: var(--ink);
  }

  /* Back: market info side */
  .card--back { background: var(--leaf); }
  .arc-line { position: absolute; inset: 0; width: 470px; height: 470px; }
  .arc-line text {
    font-family: 'Oswald', sans-serif; font-weight: 500; font-size: 24px;
    fill: var(--forest); text-transform: uppercase;
  }
  .market-name {
    position: absolute; top: 92px; left: 0; right: 0; text-align: center;
    font-family: 'Oswald', sans-serif; font-weight: 700; font-size: 60px;
    line-height: 0.98; color: var(--forest); text-transform: uppercase; letter-spacing: -0.5px;
  }
  .contact-band {
    position: absolute; top: 222px; left: 0; right: 0; height: 98px;
    background: var(--forest); display: flex; flex-direction: column;
    justify-content: center; align-items: center; gap: 4px;
    font-family: 'Montserrat', sans-serif; font-size: 23px; color: var(--paper-white);
  }
  .services {
    position: absolute; top: 334px; left: 40px; right: 40px;
    display: flex; flex-wrap: wrap; justify-content: center; gap: 10px 12px;
  }
  .service-tag {
    background: var(--forest); color: var(--tag-text);
    font-family: 'Share Tech Mono', monospace; font-size: 17px; letter-spacing: 3px;
    text-transform: uppercase; padding: 3px 6px;
  }
</style>
</head>
<body>
<main class="canvas">
  <section class="card card--front" aria-label="Card front">
    <span class="brand-dot"></span>
    <span class="brand-name">Fennel Cellar</span>
  </section>

  <section class="card card--back" aria-label="Card back">
    <svg class="arc-line" viewBox="0 0 470 470" aria-hidden="false">
      <defs>
        <path id="top-arc" d="M 58 170 A 190 190 0 0 1 412 170"/>
      </defs>
      <text><textPath href="#top-arc" startOffset="50%" text-anchor="middle">Shop online or visit us @</textPath></text>
    </svg>
    <h1 class="market-name">Willow Bend<br>Organic Market</h1>
    <div class="contact-band">
      <span class="contact-email">Ciao@fennelcellar.com.au</span>
      <span class="contact-web">Www.fennelcellar.com.au</span>
    </div>
    <ul class="services" style="list-style:none">
      <li class="service-tag">Online store</li>
      <li class="service-tag">Cooking advice</li>
      <li class="service-tag">Catering</li>
      <li class="service-tag">Ristorante and</li>
      <li class="service-tag">Information hub</li>
    </ul>
  </section>
</main>
</body>
</html>
```